looking to create a Kallah List with our logo and input the items on our list. I attached an example of what I'm looking for. Need to be similar and on nice stationary wedding paper. Simple and Elegant. Put 15% off orders.

```html
<!DOCTYPE html>
<html lang="en">
<head>
<meta charset="utf-8">
<title>Kallah List – Halden Pharmacy</title>
<link href="https://fonts.googleapis.com/css2?family=Cinzel:wght@600;700&family=Roboto:wght@400&display=swap" rel="stylesheet">
<style>
  :root{
    --blue:#2f4a9c;
    --blue-light:#8ea6dc;
    --red:#c8161d;
    --red-bright:#ee2a2a;
    --red-dark:#8f0f13;
    --ink:#2b2b2b;
    --box:#8a8a8a;
    --paper:#f4f4f5;
  }
  *{margin:0;padding:0;box-sizing:border-box}
  html,body{width:925px;height:1200px;overflow:hidden}
  body{background:var(--paper);font-family:"Roboto",Arial,sans-serif;color:var(--ink)}
  .sheet{position:relative;width:925px;height:1200px;
    background:radial-gradient(ellipse at 50% 60%,#ffffff 0%,#f1f1f2 70%,#e9e9eb 100%);overflow:hidden}
  .header-texture{position:absolute;left:0;top:0;width:925px;height:158px;
    background:linear-gradient(180deg,#f3f3f4 0%,#e6e6e8 100%)}
  .header-rule{position:absolute;left:0;width:925px}
  .header-rule.dark{top:158px;height:4px;background:var(--blue)}
  .header-rule.light{top:165px;height:3px;background:var(--blue-light)}
  .brand{position:absolute;top:46px;left:0;width:925px;display:flex;justify-content:center;align-items:center;gap:12px}
  .brand-dot{width:22px;height:22px;border-radius:50%;background:var(--red)}
  .brand-name{font-family:"Cinzel",serif;font-weight:700;font-size:38px;color:var(--red);letter-spacing:1px}
  .ribbon{position:absolute;left:170px;top:124px;width:585px;height:108px}
  .ribbon-title{position:absolute;left:230px;top:172px;width:466px;text-align:center;
    font-family:"Cinzel",serif;font-weight:700;font-size:40px;color:#fff;letter-spacing:1px}
  .section-title{position:absolute;display:flex;align-items:center;gap:14px;
    font-family:"Cinzel",serif;font-weight:700;font-size:38px;color:var(--blue);line-height:1}
  .section-title svg{flex:none}
  .checklist{position:absolute;list-style:none}
  .checklist li{position:relative;padding-left:36px;font-size:17.5px;line-height:25.4px;text-transform:uppercase}
  .checklist li::before{content:"";position:absolute;left:0;top:6px;width:11px;height:11px;border:1.3px solid var(--box);background:#fff}
  .checklist .note{display:block;font-size:13px;line-height:22.6px;margin-top:-1px}
  .checklist .inline-note{font-size:13px}
  .offer{position:absolute;left:0;top:1134px;width:925px;height:66px;
    background:linear-gradient(90deg,var(--red-dark) 0%,var(--red) 35%,var(--red-bright) 50%,var(--red) 65%,var(--red-dark) 100%);
    display:flex;justify-content:center;align-items:center;
    font-family:"Cinzel",serif;font-weight:700;color:#fff;font-size:28px;letter-spacing:.5px}
  .offer .big{font-size:35px;margin:0 8px}
</style>
</head>
<body>
<main class="sheet">
  <div class="header-texture" role="img" aria-label="Soft grey striped stationery header"></div>
  <div class="header-rule dark"></div>
  <div class="header-rule light"></div>

  <div class="brand">
    <span class="brand-dot"></span>
    <span class="brand-name">Halden Pharmacy</span>
  </div>

  <svg class="ribbon" viewBox="0 0 585 108" aria-hidden="true">
    <defs>
      <linearGradient id="band" x1="0" x2="1">
        <stop offset="0" stop-color="#b5141a"/><stop offset=".5" stop-color="#f02a2a"/><stop offset="1" stop-color="#b5141a"/>
      </linearGradient>
    </defs>
    <polygon points="4,4 120,10 120,82 22,90 50,48" fill="#b31218"/>
    <polygon points="581,4 465,10 465,82 563,90 535,48" fill="#b31218"/>
    <polygon points="60,80 120,82 120,104" fill="#6e0a0d"/>
    <polygon points="525,80 465,82 465,104" fill="#6e0a0d"/>
    <path d="M60,32 Q292,18 525,32 L525,104 Q292,96 60,104 Z" fill="url(#band)"/>
  </svg>
  <div class="ribbon-title">Kallah List</div>

  <h2 class="section-title" style="left:58px;top:274px">
    <svg width="30" height="30" viewBox="0 0 30 30" aria-hidden="true">
      <rect x="2" y="4" width="22" height="22" fill="none" stroke="#c8161d" stroke-width="2.4"/>
      <path d="M24 8h4v14h-4" fill="none" stroke="#c8161d" stroke-width="2"/>
      <path d="M13 9v12M7 15h12" stroke="#c8161d" stroke-width="2.6"/>
    </svg>
    Pharmacy
  </h2>
  <ul class="checklist" style="left:66px;top:337px;width:380px">
    <li>Hair Products<span class="note">(Hairspray; Mousse; Gel; Curlers)</span></li>
    <li>Shampoo and Conditioner</li>
    <li>Body Soap</li>
    <li>Powder</li>
    <li>Deodorant</li>
    <li>Toothbrush</li>
    <li>Toothpaste</li>
    <li>Mouthwash</li>
    <li>Dental Floss</li>
    <li>Swab-Tips</li>
    <li>Lotions; Creams;</li>
    <li>Facial Wash</li>
    <li>Cotton Balls/Pads</li>
    <li>Thermometer</li>
    <li>Allergy Medicine<span class="note">(Dryvel; Zentrix; Clarivo; Nasivo)</span></li>
    <li>Antifungal Cream/Powder</li>
    <li>Sanitary Napkins</li>
    <li>Cold Remedy Medicine<span class="note">(Feverel Cold; Mucora)</span></li>
    <li>His and Hers Vitamins</li>
    <li>Analgesics<span class="note">(Feverel; Motrex; Adwell; Etc.)</span></li>
    <li>Patch-Aids</li>
    <li>Bacitracin or Neodermin</li>
    <li>Peroxide</li>
    <li>Rubbing Alcohol</li>
    <li>Nail Clipper or Scissors</li>
    <li>Lens Solution; Rewetting Drops</li>
    <li>Lubricants <span class="inline-note">(Glydia; Smoothia; Etc.)</span></li>
  </ul>

  <h2 class="section-title" style="left:494px;top:274px">
    <svg width="30" height="30" viewBox="0 0 30 30" aria-hidden="true">
      <rect x="2" y="3" width="19" height="24" fill="none" stroke="#c8161d" stroke-width="2.4"/>
      <path d="M6 10h11M6 15h11M6 20h8" stroke="#c8161d" stroke-width="2"/>
      <path d="M25 2v18l-2 4-2-4V2z" fill="#c8161d" transform="translate(3 0)"/>
    </svg>
    Stationary
  </h2>
  <ul class="checklist" style="left:504px;top:337px;width:380px">
    <li>Pens; Pencils; Markers</li>
    <li>Writing Pads</li>
    <li>Tape</li>
    <li>Envelopes</li>
  </ul>

  <h2 class="section-title" style="left:488px;top:498px">
    <svg width="40" height="38" viewBox="0 0 40 38" aria-hidden="true">
      <path d="M2 18 Q20 -4 38 18 Q33 14 28 18 Q24 14 20 18 Q16 14 12 18 Q7 14 2 18Z" fill="#c8161d"/>
      <path d="M20 16v14q0 5-5 5t-5-5" fill="none" stroke="#c8161d" stroke-width="2.4"/>
    </svg>
    Miscellaneous
  </h2>
  <ul class="checklist" style="left:504px;top:562px;width:380px">
    <li>Umbrellas</li>
    <li>Rain Bonnet</li>
    <li>Hat Protectors</li>
    <li>Batteries</li>
    <li>Safety Pins</li>
    <li>Sewing Kits</li>
    <li>Air Fresheners</li>
    <li>Cleaning Wipes</li>
  </ul>

  <footer class="offer"><span class="big">15%</span> off all <span class="big">Kallah</span> orders</footer>
</main>
</body>
</html>
```